Wexmoor Digest - our client magazine

A quality magazine consisting of a number of bespoke articles in the first half followed by an overview of each company that form part of the group as well as details of the services offered. Vast majority of the copy is attached to provide a good overview of the content required. The magazine will require printing so quality imagery is required.

Industry/Entity Type

Recruitment

Font styles to use
Serif

Colors
0355a3
6b449b
3276b5
876aae
a64599
00a990
5c5c5c
000000
474747

Requirements
Must have
• Bringing the copy to life through flow charts and/or diagrams where possible.

```html
<!DOCTYPE html>
<html lang="en">
<head>
<meta charset="utf-8">
<title>Wexmoor Digest – Welcome message from MD</title>
<link rel="stylesheet" href="https://fonts.googleapis.com/css2?family=Noticia+Text:wght@400&family=Great+Vibes&display=swap">
<style>
  :root {
    --backdrop: #e9e6e2;
    --page: #ffffff;
    --ink: #000000;
    --ink-soft: #474747;
    --rule: #5c5c5c;
    --brand-blue: #0355a3;
    --brand-blue-soft: #3276b5;
    --brand-purple: #6b449b;
    --brand-purple-soft: #876aae;
    --photo-night: #0b0c0a;
    --photo-foliage: #1c2218;
    --photo-timber: #a8692c;
    --photo-amber: #d08a3e;
    --photo-suit: #2a2628;
    --photo-paper: #d9cbb6;
    --portrait-tone: #a7978a;
  }
  * { box-sizing: border-box; margin: 0; padding: 0; }
  html, body { width: 1200px; height: 982px; overflow: hidden; background: var(--backdrop); }
  .spread {
    position: absolute; left: 40px; top: 40px; width: 1120px; height: 902px;
    display: flex; box-shadow: 0 10px 30px rgba(0,0,0,.18);
  }
  .page { width: 560px; height: 100%; position: relative; }
  .page--photo {
    background:
      radial-gradient(ellipse 26% 20% at 30% 74%, var(--photo-paper) 0%, rgba(217,203,182,.55) 45%, transparent 100%),
      radial-gradient(ellipse 22% 30% at 34% 30%, var(--photo-amber) 0%, rgba(168,105,44,.55) 45%, transparent 100%),
      radial-gradient(ellipse 30% 10% at 40% 22%, rgba(168,105,44,.7) 0%, transparent 100%),
      radial-gradient(ellipse 40% 45% at 72% 62%, var(--photo-suit) 0%, transparent 100%),
      radial-gradient(ellipse 20% 14% at 76% 30%, rgba(168,105,44,.45) 0%, transparent 100%),
      linear-gradient(180deg, var(--photo-foliage) 0%, var(--photo-night) 100%);
  }
  .page--letter { background: var(--page); padding: 88px 100px 0 84px; }
  .letter-header {
    display: flex; justify-content: space-between; align-items: flex-end;
    height: 112px; border-bottom: 1px solid var(--brand-blue);
  }
  .letter-title {
    font-family: "Great Vibes", cursive; font-weight: 400; font-size: 27px; line-height: 1.05;
    color: var(--ink); padding: 0 0 28px 12px;
  }
  .portrait {
    width: 96px; height: 108px; margin-right: 14px;
    background: linear-gradient(180deg, #f2efec 0%, var(--portrait-tone) 100%);
  }
  .letter-body {
    margin-top: 10px; font-family: "Noticia Text", serif; font-size: 11.6px; line-height: 1.4;
    color: var(--ink); hyphens: auto; padding-right: 6px;
  }
  .letter-body p { margin: 0; }
  .letter-body p + p { margin-top: 0; }
  .signature {
    margin-top: 30px; font-family: "Great Vibes", cursive; font-size: 28px; line-height: 1;
    color: var(--brand-purple);
  }
  .sign-role {
    font-family: "Noticia Text", serif; font-size: 11px; line-height: 1.5;
    color: var(--ink-soft); margin-top: 8px;
  }
  .page-foot {
    position: absolute; left: 84px; right: 150px; bottom: 62px;
    border-top: 1px solid var(--brand-blue-soft);
  }
</style>
</head>
<body>
  <main class="spread">
    <section class="page page--photo" role="img" aria-label="Photograph of a bearded man in a dark suit and sunglasses reading a business newspaper in front of a sunlit wooden window frame"></section>
    <section class="page page--letter">
      <header class="letter-header">
        <h1 class="letter-title">Welcome message<br>from MD</h1>
        <div class="portrait" role="img" aria-label="Headshot portrait of the managing director"></div>
      </header>
      <div class="letter-body">
        <p>Hello and welcome to this latest edition of Wexmoor Digest.</p>
        <p>In this issue, we are considering the importance of “brand” throughout the recruitment process. As Headhunters, our brand and reputation have always been key to our business. It’s important that candidates know and respect us, and that our clients are happy to recommend us to other companies. However, in recent years it has become increasingly important for both clients and candidates to also consider their own brand very carefully.</p>
        <p>With UK unemployment at record low levels, the competition between companies to attract and retain the top talent is getting fiercer all the time. Candidates will often have multiple job options to choose between. The reputation, culture and working environment of each potential employer therefore needs to be carefully researched to ensure the right choice is made. Developing an attractive and effective Employer Brand and Marketing strategy is therefore essential for all companies.</p>
        <p>On the candidate side, brand is equally important when competing for the most attractive roles. This poses some interesting challenges in the modern world. As social media has become an integral part of life today, the separation between our personal and professional lives is being reduced. Candidates need to be aware that their online life is part of their personal brand and can be important for their career.</p>
        <p>We will consider these issues and more over the next few pages. As always, please do not hesitate to contact us with any questions or comments which arise.</p>
        <p>I hope you enjoy reading this issue and look forward to working with you soon.</p>
        <p>Sincerely,</p>
      </div>
      <div class="signature">Alan Reeve</div>
      <div class="sign-role">Co-Founder &amp; CEO<br>The Harwick Group</div>
      <div class="page-foot"></div>
    </section>
  </main>
</body>
</html>
```